Company Website

We need an interactive website designed that for new company. Our company is in the Automotive fleet maintenance business. We have wide ranging customers in many industries e.g Aviation industry, construction industry, transportation etc.
We would like the website to have login accounts where customers can register, login and access their service history. Also we would like to have an appointment system where customers could schedule appointments, once appointments are made that time would no longer be available to be selected as it would be booked etc.

The website should also be updatable and provide areas for showcasing
Our services
Products/parts (possibly store front)
Customer feedback
Appointments
Our customers (where our customers can advertise or be showcased)
About us
Contacts
gallery

We would like designs that have a modern, corporate feel, One that is user friendly.
prefer a design that does not look like a template.

Target Market(s)

Medium to large companies, small business owners and the general motoring public.

Industry/Entity Type

Construction

Requirements
Must have
• Customer login set up so a database of customer vehicle maintenance history as well as the ability to schedule repairs via their account. They could also check the status of a repair.
Nice to have
• Photo gallery to show case current projects.
Our customers page where we can show case our clients they could also post their events on there, promotions etc.

The theme Should be something that's reflective of our core business; fleet maintenance. It would be nice to capture some sort of background in there that depicts some of that for example mixer trucks, tractors,loaders excavators forklifts cars trucks. That's what we deal with. It's up to the designer to capture the Essence of this as much as possible. Impress me.
Should not have
• Would prefer a custom website not a template.

```html
<!DOCTYPE html>
<html lang="en">
<head>
<meta charset="utf-8">
<title>Steadwell Fleet &amp; Auto Maintenance</title>
<link href="https://fonts.googleapis.com/css2?family=Arimo:wght@400;700&family=Roboto+Condensed:wght@300;400;700&display=swap" rel="stylesheet">
<style>
:root{
  --red:#c4000d;
  --red-dark:#7a0007;
  --band:#8a0009;
  --page:#f3f1f1;
  --header:#f7f7f7;
  --ink:#222;
  --muted:#555;
  --pink:#f47f74;
  --slate:#2f3b47;
  --footer:#2a2424;
  --footer-text:#6d6565;
}
*{box-sizing:border-box;margin:0;padding:0}
html,body{width:1200px;height:891px;overflow:hidden}
body{position:relative;background:var(--page);font-family:"Arimo",Arial,sans-serif;color:var(--ink)}
.abs{position:absolute}
.site-header{left:0;top:0;width:1200px;height:81px;background:var(--header)}
.brand{left:102px;top:14px;font-family:"Roboto Condensed",Arial,sans-serif;color:var(--red)}
.brand-name{font-size:28px;font-weight:700;letter-spacing:1px;line-height:30px}
.brand-tag{font-size:10px;font-weight:700;letter-spacing:.3px;margin-top:2px}
.social{top:13px;display:flex;gap:20px;left:1004px}
.social span{width:20px;height:20px;background:#d4d4d4;border-radius:50%}
.main-nav{left:337px;top:38px;height:43px;display:flex;font-size:14px}
.main-nav a{color:var(--ink);text-decoration:none;padding:14px 15px 0;height:43px}
.main-nav a.active{background:var(--red);color:#fff;border-radius:5px 5px 0 0;padding:14px 17px 0}
.account{left:1004px;top:52px;font-size:14px;color:var(--red-dark)}
.hero-band{left:0;top:81px;width:1200px;height:459px;background:linear-gradient(180deg,#8d000a,#77050b)}
.slider{left:96px;top:92px;width:1023px;height:436px;background:#fff;border-radius:6px;padding:6px}
.slide-photo{width:100%;height:100%;background:linear-gradient(100deg,#5a6c86 0%,#8b9bb3 30%,#6b7078 55%,#2a2f38 75%,#1a1c22 100%)}
.caption{left:101px;top:339px;width:656px;height:142px;background:rgba(40,40,40,.55)}
.caption p{position:absolute;left:27px;top:27px;width:420px;font-family:"Roboto Condensed",Arial,sans-serif;font-weight:300;font-size:19px;line-height:24px;color:#eee}
.cta{left:333px;top:404px;width:386px;height:94px;border:3px solid #fff;border-radius:7px;background:linear-gradient(180deg,#d4000f,#8e0008);color:#fff}
.cta svg{position:absolute;left:55px;top:20px}
.cta-title{position:absolute;left:127px;top:30px;font-family:"Roboto Condensed",Arial,sans-serif;font-size:24px}
.cta-sub{position:absolute;left:292px;top:60px;font-size:8px;color:#444}
.arrow{width:25px;height:25px;background:var(--slate);top:284px}
.arrow svg{display:block;margin:7px auto}
.card{top:571px;width:230px}
.card-photo{height:140px;position:relative}
.read-more{position:absolute;left:0;bottom:0;display:flex;height:37px}
.read-more b{background:var(--pink);color:#fff;font-family:"Roboto Condensed",Arial,sans-serif;font-size:13px;width:95px;line-height:37px;text-align:center}
.read-more i{background:var(--slate);width:35px;display:flex;align-items:center;justify-content:center}
.card h2{font-family:"Roboto Condensed",Arial,sans-serif;font-weight:400;font-size:19px;color:var(--red-dark);margin-top:21px}
.card p{font-size:12px;line-height:18px;margin-top:8px;padding-left:2px}
.customers{left:911px;top:571px;width:209px;height:236px;background:#e6e3e3;border-radius:5px;overflow:hidden}
.customers h3{background:var(--red);color:#fff;font-family:"Roboto Condensed",Arial,sans-serif;font-weight:400;font-size:19px;text-align:center;height:36px;line-height:36px}
.badge{position:absolute;left:35px;width:138px;height:43px;background:#fff}
.badge span{position:absolute;left:10px;top:10px;width:118px;height:23px;background:#cfcfcf;border-radius:3px}
.feedback{left:1159px;top:488px;width:41px;height:102px;background:var(--slate);border:2px solid #fff;border-right:0;border-radius:4px 0 0 4px;color:#fff}
.feedback span{position:absolute;left:9px;top:82px;transform:rotate(-90deg);transform-origin:left top;font-size:14px}
.footer-rule{left:0;top:842px;width:1200px;height:7px;background:#e9e6e6}
.site-footer{left:0;top:849px;width:1200px;height:42px;background:var(--footer)}
.site-footer p{position:absolute;left:109px;top:14px;font-size:13px;color:var(--footer-text)}
.footer-brand{position:absolute;left:968px;top:2px;width:150px;text-align:center;font-family:"Roboto Condensed",Arial,sans-serif;color:#fff;font-weight:700;line-height:1}
.footer-brand-name{display:block;font-size:21px;letter-spacing:1px}
.footer-brand-tag{display:block;font-size:8px;letter-spacing:.3px;margin-top:3px}
</style>
</head>
<body>
<header class="site-header abs">
  <div class="brand abs">
    <div class="brand-name">STEADWELL</div>
    <div class="brand-tag">FLEET &amp; AUTO MAINTENANCE</div>
  </div>
  <div class="social abs" aria-label="Social links">
    <span></span><span></span>
    <svg width="22" height="16" viewBox="0 0 22 16" aria-label="Email"><rect x="1" y="1" width="20" height="14" fill="none" stroke="#cfcfcf" stroke-width="1.5"/><path d="M1 1l10 8 10-8" fill="none" stroke="#cfcfcf" stroke-width="1.5"/></svg>
  </div>
  <nav class="main-nav abs">
    <a href="#">Our services</a>
    <a href="#" class="active">Products/parts</a>
    <a href="#">Our customers</a>
    <a href="#">About us</a>
    <a href="#">Contacts</a>
  </nav>
  <div class="account abs">Register &nbsp;/&nbsp; Login</div>
</header>

<section class="hero-band abs"></section>
<div class="slider abs"><div class="slide-photo" role="img" aria-label="Night street with cars and blurred city lights"></div></div>
<div class="caption abs"><p>Lorem Ipsum is simply dummy text of the printing and typesetting industry.</p></div>
<a class="cta abs" href="#">
  <svg width="44" height="44" viewBox="0 0 44 44"><path d="M36 22a14 14 0 1 1-5-10.7" fill="none" stroke="#111" stroke-width="5"/><path d="M33 4l1 11-11-1z" fill="#111"/><path d="M20 14v10h8" fill="none" stroke="#111" stroke-width="4"/></svg>
  <span class="cta-title">Make an Appointment.</span>
  <span class="cta-sub">Click here</span>
</a>
<div class="arrow abs" style="left:71px"><svg width="8" height="11"><path d="M6 1L2 5.5 6 10" fill="none" stroke="#fff" stroke-width="1.5"/></svg></div>
<div class="arrow abs" style="left:1119px"><svg width="8" height="11"><path d="M2 1l4 4.5L2 10" fill="none" stroke="#fff" stroke-width="1.5"/></svg></div>

<article class="card abs" style="left:108px">
  <div class="card-photo" role="img" aria-label="Mechanic working under a car bonnet" style="background:linear-gradient(120deg,#4a5058,#9aa2ab 50%,#3d4a6a)">
    <div class="read-more"><b>READ MORE</b><i><svg width="8" height="11"><path d="M2 1l4 4.5L2 10" fill="none" stroke="#fff" stroke-width="1.5"/></svg></i></div>
  </div>
  <h2>Our services</h2>
  <p>Lorem Ipsum is simply dummy text of the printing and typesetting industry. Lorem Ipsum.</p>
</article>
<article class="card abs" style="left:377px">
  <div class="card-photo" role="img" aria-label="Hand cleaning a car wheel rim" style="background:linear-gradient(120deg,#6b4a3c,#9a9ea4 45%,#2a2a2c)">
    <div class="read-more"><b>READ MORE</b><i><svg width="8" height="11"><path d="M2 1l4 4.5L2 10" fill="none" stroke="#fff" stroke-width="1.5"/></svg></i></div>
  </div>
  <h2>Products / Parts</h2>
  <p>Lorem Ipsum is simply dummy text of the printing and typesetting industry. Lorem Ipsum.</p>
</article>
<article class="card abs" style="left:648px">
  <div class="card-photo" role="img" aria-label="Grid of assorted car photos" style="background:linear-gradient(120deg,#cfd3d8,#b34a4a 40%,#e8e8e8 60%,#7a7e85)">
    <div class="read-more"><b>READ MORE</b><i><svg width="8" height="11"><path d="M2 1l4 4.5L2 10" fill="none" stroke="#fff" stroke-width="1.5"/></svg></i></div>
  </div>
  <h2>Gallery</h2>
  <p>Lorem Ipsum is simply dummy text of the printing and typesetting industry. Lorem Ipsum.</p>
</article>

<aside class="customers abs">
  <h3>Our customers</h3>
  <div class="badge" style="top:61px"><span></span></div>
  <div class="badge" style="top:115px"><span></span></div>
  <div class="badge" style="top:172px"><span></span></div>
</aside>

<div class="feedback abs"><span>Feedback</span></div>

<div class="footer-rule abs"></div>
<footer class="site-footer abs">
  <p>STEADWELL © 2013 | Privacy Policy</p>
  <div class="footer-brand">
    <span class="footer-brand-name">STEADWELL</span>
    <span class="footer-brand-tag">FLEET &amp; AUTO MAINTENANCE</span>
  </div>
</footer>
</body>
</html>
```